Fatigued and Overloaded by COVID Messages? We need original illustrations to show that.

Everywhere you look there are messages about COVID. That is leading many people to feel fatigued and overloaded by the messages.

We surveyed U.S. adults March 20th - 24th, 2020 and measured message fatigue, information overload, perceived repetition, and perceived exaggeration. Here is how participants responded:

When it comes to coronavirus . . .
55% feel exhausted by all the messages.
54% feel overloaded by the amount of information.
51% feel that the messages are repetitive.
47% feel like messages exaggerate how bad it is.

In other words, almost half of U.S. adults show signs of message fatigue, information overload, perceived message repetition, and perceived message exaggeration.

We will continue to survey 400 adults every week for the next 16 weeks. Each time we will measure message fatigue, information overload, perceived repetition, and perceived exaggeration. We expect that it will increase over time.

What are we looking for? We need innovative and original illustrations that attempt to communicate these findings. The illustrations would visualize message fatigue, information overload, perceived message repetition, and perceived message exaggeration.

What sort of visual are we looking for? Our preference is for an original illustration (or set of illustrations). Our preference is for creative and powerful illustrations, but we are also open to the creative and well-executed infographics.

We need these images fast . We will award monetary prizes to the 3 best designs. If we like more than that, then we might purchase more (e.g., in past contests, we have purchased as many as 30 designs).

What we will need:
(1) The illustrations must be original and we will need the photoshop and/or illustrator files for all artwork. (By original, we mean that the illustrations are 100% created by you. Our organization requires that we utilize only original illustrated work. We have had issues with free imagery being pirated and reposted as free. We sidestep that issue by just having everything created.)

(2) The illustration should say, somewhere: "Based on a survey of 400 U.S. adults conducted March 20 - 24th, 2020."

(3) We will have almost 4 months worth of data by the time this is done. In other words, the illustrations might be able to help us present that weekly data.

(4) We have conducted other Artvendo projects. It might be helpful to examine designs we liked in the past. For example, here is another COVID project we just finished:

https://jobs.artvendo-example.com/job/5162048

Target Market(s)

U.S. adults

Requirements
Must have
• Original illustrations. Mobile friendly design. People will view this on their smartphones.
Nice to have
• A design that we can use to communicate the data across time.

```html
<!DOCTYPE html>
<html lang="en">
<head>
<meta charset="utf-8">
<title>Fatigued and Overloaded by COVID Messages?</title>
<link rel="stylesheet" href="https://fonts.googleapis.com/css2?family=Bree+Serif&display=swap">
<style>
  :root {
    --page: #c9fbfc;
    --panel: #92f3f9;
    --stat-box: #22d5ea;
    --title-blue: #5a9be2;
    --yellow: #fdf78c;
    --band-yellow: #fcfa9c;
    --intro-text: #189fb6;
    --footer-text: #58b6e2;
    --white: #ffffff;
  }
  * { box-sizing: border-box; margin: 0; padding: 0; }
  html, body { width: 691px; height: 1200px; overflow: hidden; }
  body {
    background: var(--page);
    font-family: "Bree Serif", Georgia, serif;
    position: relative;
  }
  .title-panel {
    position: absolute; left: 15px; top: 0; width: 660px; height: 198px;
    background: var(--panel);
  }
  .title-line {
    position: absolute; left: 0; width: 100%; text-align: center;
    color: var(--title-blue); font-size: 57px; line-height: 1; white-space: nowrap;
  }
  .title-line.first { top: 40px; }
  .title-line.second { top: 104px; }
  .covid-mark {
    display: inline-block; background: var(--stat-box); color: var(--yellow);
    font-size: 78px; padding: 4px 10px 6px; margin: 0 4px; vertical-align: middle;
    line-height: 1;
  }
  .intro-band {
    position: absolute; left: 15px; top: 208px; width: 660px; height: 162px;
    background: var(--band-yellow); padding: 9px 26px 0 26px;
    color: var(--intro-text); font-size: 13.6px; line-height: 25.5px;
  }
  .intro-band p + p { margin-top: 9px; }
  .findings-panel {
    position: absolute; left: 15px; top: 383px; width: 660px; height: 742px;
    background: var(--panel);
  }
  .illustration { position: absolute; border-radius: 6px; }
  .illo-laptop { left: 40px; top: 392px; width: 315px; height: 208px;
    background: linear-gradient(135deg, #b8f7fb, #a6ecf0 60%, #c9f3d0); }
  .illo-megaphone { left: 392px; top: 535px; width: 282px; height: 228px;
    background: linear-gradient(160deg, #c2f8fb, #a4e8f4 55%, #8fb8e8); }
  .illo-television { left: 42px; top: 725px; width: 268px; height: 218px;
    background: linear-gradient(135deg, #c7eef4, #a9d8e6 60%, #b9e8c6); }
  .illo-phone { left: 385px; top: 905px; width: 260px; height: 220px;
    background: linear-gradient(160deg, #b6f4fa, #a7e4ee 55%, #f2b8e2); }
  .stat {
    position: absolute; background: var(--stat-box);
    display: flex; align-items: center;
  }
  .stat-figure {
    color: var(--yellow); font-size: 58px; line-height: 1; flex: none;
  }
  .stat-label {
    color: var(--white); font-size: 27px; line-height: 29px;
  }
  .stat-exhausted { left: 364px; top: 400px; width: 327px; height: 120px; padding-left: 14px; }
  .stat-exhausted .stat-figure { width: 124px; }
  .stat-overloaded { left: 0; top: 609px; width: 354px; height: 109px; padding-left: 23px; }
  .stat-overloaded .stat-figure { width: 135px; }
  .stat-exaggerate { left: 339px; top: 766px; width: 352px; height: 118px; padding-left: 6px; }
  .stat-exaggerate .stat-figure { width: 124px; }
  .stat-repetitive { left: 0; top: 966px; width: 354px; height: 116px; padding-left: 23px; }
  .stat-repetitive .stat-figure { width: 138px; }
  .footer-band {
    position: absolute; left: 15px; top: 1140px; width: 660px; height: 60px;
    background: var(--band-yellow); color: var(--footer-text);
    font-size: 17.5px; text-align: center; line-height: 60px;
  }
</style>
</head>
<body>
  <header class="title-panel">
    <h1 class="title-line first">Fatigued and Overloaded</h1>
    <div class="title-line second">by <span class="covid-mark">COVID</span> Messages?</div>
  </header>

  <section class="intro-band">
    <p>Everywhere you look there are messages about COVID. That is leading many people to feel fatigued and overloaded by the messages.</p>
    <p>We surveyed U.S. adults March 20th - 24th, 2020 and measured message fatigue, information overload, perceived repetition, and perceived exaggeration. Almost half of U.S. adults show signs of message fatigue, information overload, perceived message repetition, and perceived message exaggeration.</p>
  </section>

  <section class="findings-panel"></section>

  <div class="illustration illo-laptop" role="img" aria-label="Illustration of a tired woman at a laptop with virus words flying out of the screen"></div>
  <div class="illustration illo-megaphone" role="img" aria-label="Illustration of a man covering his ears beneath a megaphone blaring virus messages"></div>
  <div class="illustration illo-television" role="img" aria-label="Illustration of a retro television showing a breaking news report about the virus"></div>
  <div class="illustration illo-phone" role="img" aria-label="Illustration of an annoyed woman looking at her phone with virus chat bubbles"></div>

  <div class="stat stat-exhausted">
    <span class="stat-figure">55%</span>
    <span class="stat-label">feel exhausted<br>by all the<br>messages</span>
  </div>
  <div class="stat stat-overloaded">
    <span class="stat-figure">54%</span>
    <span class="stat-label">feel overloaded<br>by the amount<br>of information</span>
  </div>
  <div class="stat stat-exaggerate">
    <span class="stat-figure">47%</span>
    <span class="stat-label">feel like messages<br>exaggerate how<br>bad it is.</span>
  </div>
  <div class="stat stat-repetitive">
    <span class="stat-figure">51%</span>
    <span class="stat-label">feel that the<br>messages are<br>repetitive</span>
  </div>

  <footer class="footer-band">Based on a survey of 400 U.S. adults conducted March 20 - 24th, 2020.</footer>
</body>
</html>
```